I need a new business card design for my pharmacy.

I need a business card design. I will include my logo.
The card needs to be readable. I prefer to have my logo on one side along with my website, the other side includes the other information. Please use combination of black, neon green, white, and silver. This needs to catch the eye but yet be clearly visible and legible. Thanks

Industry/Entity Type

Pharmacy

Contact Information for Business Card

It needs to have the following information listed:
Mel's Apothecary Owner/Pharm D.
7134 North Brook Lane
Sioux Falls, SD 57231
Phone 605-318-6207
Fax 605-318-6209
email: mel@melsapothecary-example.com
www.melsapothecary-example.com
Store hours Monday-Friday 8 am- 7 pm
Saturday 8 am- 12 pm
Sunday Closed
Please utilize the colors black, white, and neon green, maybe silver.

Requirements
Must have
• It needs to be easily readable!
Nice to have
• It should catch the eye.
Should not have
• Do not use any other colors except listed: black, neon green, white, & silver.

```html
<!DOCTYPE html>
<html lang="en">
<head>
<meta charset="utf-8">
<title>Mel's Apothecary – Business Card</title>
<link rel="stylesheet" href="https://fonts.googleapis.com/css2?family=Open+Sans:wght@400;600&display=swap">
<style>
  :root {
    --neon: #9cc83a;
    --neon-light: #c9e15c;
    --neon-dark: #86b52a;
    --ink: #1b1b1b;
    --white: #ffffff;
    --silver: #dcdedf;
    --backdrop: #e9e9e7;
  }
  * { box-sizing: border-box; margin: 0; padding: 0; }
  html, body { width: 1200px; height: 892px; overflow: hidden; }
  body {
    background: var(--backdrop);
    font-family: "Open Sans", Arial, sans-serif;
    color: var(--ink);
    position: relative;
  }
  .card {
    position: absolute;
    left: 250px;
    width: 700px;
    height: 400px;
    border-radius: 4px;
    box-shadow: 0 4px 14px rgba(0,0,0,0.18);
    overflow: hidden;
  }

  /* Front */
  .card-front { top: 31px; background: var(--white); }
  .brand-block {
    position: absolute; left: 40px; top: 165px;
    display: flex; align-items: center; gap: 16px;
    white-space: nowrap;
  }
  .brand-dot {
    width: 30px; height: 30px; border-radius: 50%;
    background: var(--neon);
  }
  .brand-divider { width: 1px; height: 54px; background: var(--neon); }
  .brand-name {
    font-size: 30px; font-weight: 600; color: var(--neon);
    letter-spacing: -0.5px;
  }
  .owner-block { position: absolute; left: 400px; top: 48px; white-space: nowrap; }
  .owner-company { font-size: 25px; color: var(--neon); line-height: 1.2; }
  .owner-title { font-size: 16px; color: var(--ink); margin-top: 2px; }
  .front-rule {
    position: absolute; left: 300px; top: 132px;
    width: 380px; height: 1.5px; background: var(--ink);
  }
  .contact-list {
    position: absolute; left: 400px; top: 168px;
    list-style: none; font-size: 14px; line-height: 25px;
    white-space: nowrap;
  }
  .contact-list li { display: flex; align-items: center; gap: 10px; }
  .contact-icon {
    width: 12px; height: 12px; background: var(--neon);
    border-radius: 2px; flex: none;
  }
  .address-band {
    position: absolute; left: 0; right: 0; bottom: 0; height: 92px;
    background: linear-gradient(180deg, var(--neon-light), var(--neon));
    display: flex; align-items: center; padding-left: 200px; gap: 14px;
    white-space: nowrap;
  }
  .address-band .pin-box {
    width: 20px; height: 20px; background: var(--ink); flex: none;
    display: flex; align-items: center; justify-content: center; border-radius: 2px;
  }
  .address-text { font-size: 18px; color: var(--ink); }

  /* Back */
  .card-back {
    top: 461px; background: var(--silver); padding: 14px;
  }
  .back-panel {
    position: relative; width: 100%; height: 100%;
    background: radial-gradient(ellipse at 40% 40%, var(--neon-light) 0%, #b4d64a 55%, var(--neon) 100%);
  }
  .back-brand {
    position: absolute; left: 42px; top: 40px;
    display: flex; align-items: center; gap: 20px;
    white-space: nowrap;
  }
  .back-brand .brand-dot { background: var(--ink); width: 36px; height: 36px; }
  .back-brand .brand-divider { background: var(--ink); height: 68px; }
  .back-brand .brand-name { color: var(--ink); font-size: 44px; }
  .hours-heading {
    position: absolute; left: 42px; right: 42px; top: 160px;
    display: flex; align-items: center; gap: 16px;
    font-size: 30px; white-space: nowrap;
  }
  .hours-heading .rule { flex: 1; height: 2px; background: var(--ink); }
  .hours-heading .rule-short { flex: 0 0 40px; }
  .hours-list {
    position: absolute; left: 110px; top: 224px;
    list-style: none; font-size: 20px; line-height: 32px;
    white-space: nowrap;
  }
</style>
</head>
<body>

<section class="card card-front" aria-label="Business card front">
  <div class="brand-block">
    <span class="brand-dot"></span>
    <span class="brand-divider"></span>
    <span class="brand-name">Mel's Apothecary</span>
  </div>

  <div class="owner-block">
    <div class="owner-company">Mel's Apothecary</div>
    <div class="owner-title">Owner/Pharm D.</div>
  </div>

  <div class="front-rule" aria-hidden="true"></div>

  <ul class="contact-list">
    <li><span class="contact-icon"></span>605-318-6207</li>
    <li><span class="contact-icon"></span>605-318-6209</li>
    <li><span class="contact-icon"></span>mel@melsapothecary-example.com</li>
    <li><span class="contact-icon"></span>www.melsapothecary-example.com</li>
  </ul>

  <div class="address-band">
    <span class="pin-box">
      <svg width="10" height="12" viewBox="0 0 10 12" aria-hidden="true">
        <path d="M5 0C2.2 0 0 2.2 0 4.8 0 8.2 5 12 5 12s5-3.8 5-7.2C10 2.2 7.8 0 5 0z" fill="#9cc83a"/>
        <circle cx="5" cy="4.8" r="1.8" fill="#1b1b1b"/>
      </svg>
    </span>
    <span class="address-text">7134 North Brook Lane Sioux Falls, SD 57231</span>
  </div>
</section>

<section class="card card-back" aria-label="Business card back">
  <div class="back-panel">
    <div class="back-brand">
      <span class="brand-dot"></span>
      <span class="brand-divider"></span>
      <span class="brand-name">Mel's Apothecary</span>
    </div>

    <div class="hours-heading">
      <span class="rule rule-short"></span>
      <span>Store hours :</span>
      <span class="rule"></span>
    </div>

    <ul class="hours-list">
      <li>Monday-Friday 8 am- 7 pm</li>
      <li>Saturday 8 am- 12 pm</li>
      <li>Sunday Closed</li>
    </ul>
  </div>
</section>

</body>
</html>
```